Australian Trucking Company Requires Professional Looking Stationary

We require a professional looking stationary design that incorporates our newly designed logo.

Our business, called "Vell Haulage Contracting", provides contracting work, transport and logistics to business in Western Australia particularly with links to the mining sector.

We are a small business looking to expand and our new logo and our new stationary will help develop our brand image in our market place.

Target Market(s)

Businesses and Corporation with links to the Mining Sector

Industry/Entity Type

Small Business

Requirements
Must have
• The letterhead must have the following details:
The new logo

Text saying: "Vell Haulage Pty Ltd (ACN 582 306 917) ATF The Vell Discretionary Trust T/AS"
"ABN 71 840 239 568"
Address "P.O Box 817 Ashbury WA, 6912"
Phone: 08 9172 5840
Email: vellhaul@mailnest.com.au

The text on the letterhead should be editable as the details are likely to change in the near future. Provision should be made for a website address all though one isn't available at the moment.

The styling, layout and font text is entirely up to the designer.

```html
<!DOCTYPE html>
<html lang="en">
<head>
<meta charset="utf-8">
<title>Vell Haulage Contracting – Business Cards</title>
<link rel="stylesheet" href="https://fonts.googleapis.com/css2?family=Arimo:wght@400;700&display=swap">
<style>
  :root {
    --stage: #e4e4e4;
    --card-white: #f7f7f7;
    --red: #d1232a;
    --red-deep: #a3161b;
    --red-band: #b81c22;
    --charcoal: #4a4a4a;
    --charcoal-deep: #383838;
    --charcoal-band: #424242;
    --ink: #333333;
    --muted: #6a6a6a;
    --white: #ffffff;
  }
  * { margin: 0; padding: 0; box-sizing: border-box; }
  html, body { width: 1200px; height: 872px; overflow: hidden; }
  body {
    background: var(--stage);
    font-family: "Arimo", Arial, sans-serif;
    position: relative;
  }
  .card {
    position: absolute;
    width: 440px;
    height: 250px;
    border-radius: 16px;
    overflow: hidden;
    box-shadow: 0 4px 14px rgba(0,0,0,0.18);
  }
  .card-front { background: var(--card-white); }
  .card-front.first { left: 150px; top: 150px; }
  .card-front.second { left: 150px; top: 470px; }
  .card-back.red {
    left: 620px; top: 150px;
    background: linear-gradient(135deg, var(--red), var(--red-deep));
  }
  .card-back.charcoal {
    left: 620px; top: 470px;
    background: linear-gradient(135deg, var(--charcoal), var(--charcoal-deep));
  }

  /* front logo strip */
  .logo-strip {
    position: absolute;
    left: 78px; top: 26px; right: 0;
    height: 56px;
    background: linear-gradient(90deg, var(--red), var(--red-deep));
    display: flex;
    align-items: center;
    padding-left: 12px;
  }
  .logo-mark-square {
    position: absolute;
    left: 26px; top: 34px;
    width: 40px; height: 40px;
    background: var(--charcoal);
  }
  .wordmark {
    color: var(--white);
    font-weight: 700;
    text-transform: uppercase;
    line-height: 1;
  }
  .logo-strip .wordmark { font-size: 15px; line-height: 16px; }

  .person-name { color: var(--red); font-size: 20px; font-weight: 400; }
  .person-role { color: var(--ink); font-size: 13px; margin-top: 3px; }

  .person.left { position: absolute; left: 26px; top: 112px; }
  .person.right { position: absolute; left: 236px; top: 104px; }

  .details {
    position: absolute;
    font-size: 9px;
    line-height: 12px;
    color: var(--muted);
  }
  .first .details { left: 26px; top: 166px; }
  .second .details { left: 26px; top: 172px; }
  .details .abn { margin-left: 14px; }
  .contact-line { display: flex; align-items: center; gap: 4px; }
  .contact-line svg { width: 9px; height: 9px; fill: var(--red); flex: none; }

  /* back */
  .back-band {
    position: absolute;
    left: 0; right: 0; top: 78px;
    height: 100px;
    display: flex;
    align-items: center;
    justify-content: center;
    gap: 18px;
  }
  .red .back-band { background: var(--red-band); }
  .charcoal .back-band { background: var(--charcoal-band); }
  .back-band .square {
    width: 46px; height: 46px;
    border: 3px solid var(--white);
  }
  .back-band .wordmark { font-size: 26px; line-height: 26px; }
</style>
</head>
<body>

  <section class="card card-front first">
    <div class="logo-mark-square"></div>
    <div class="logo-strip"><div class="wordmark">Vell Haulage<br>Contracting</div></div>
    <div class="person left">
      <div class="person-name">Martin Calder</div>
      <div class="person-role">President</div>
    </div>
    <div class="details">
      <div>Vell Haulage Pty Ltd (ACN 582 306 917)</div>
      <div>ATF The Vell Discretionary Trust T/AS<span class="abn">ABN 71 840 239 568</span></div>
      <div class="contact-line"><svg viewBox="0 0 10 10"><path d="M5 0 10 5H8.5V10H6V7H4V10H1.5V5H0Z"/></svg>P.O Box 817 Ashbury WA, 6912</div>
      <div class="contact-line"><svg viewBox="0 0 10 10"><path d="M2 0h2l1 3-1.5 1a6 6 0 0 0 2.5 2.5L7 5l3 1v2c0 1-1 2-2 2A8 8 0 0 1 0 2c0-1 1-2 2-2z"/></svg>08 9172 5840</div>
      <div class="contact-line"><svg viewBox="0 0 10 10"><path d="M0 2h10v6H0zM0 2l5 3.5L10 2" stroke="#fff" stroke-width=".8"/></svg>vellhaul@mailnest.com.au</div>
    </div>
  </section>

  <section class="card card-front second">
    <div class="logo-mark-square"></div>
    <div class="logo-strip"><div class="wordmark">Vell Haulage<br>Contracting</div></div>
    <div class="person right">
      <div class="person-name">Martin Calder</div>
      <div class="person-role">President</div>
    </div>
    <div class="details">
      <div>Vell Haulage Pty Ltd (ACN 582 306 917)</div>
      <div>ATF The Vell Discretionary Trust T/AS<span class="abn">ABN 71 840 239 568</span></div>
      <div class="contact-line"><svg viewBox="0 0 10 10"><path d="M5 0 10 5H8.5V10H6V7H4V10H1.5V5H0Z"/></svg>P.O Box 817 Ashbury WA, 6912</div>
      <div class="contact-line"><svg viewBox="0 0 10 10"><path d="M2 0h2l1 3-1.5 1a6 6 0 0 0 2.5 2.5L7 5l3 1v2c0 1-1 2-2 2A8 8 0 0 1 0 2c0-1 1-2 2-2z"/></svg>08 9172 5840</div>
      <div class="contact-line"><svg viewBox="0 0 10 10"><path d="M0 2h10v6H0zM0 2l5 3.5L10 2" stroke="#fff" stroke-width=".8"/></svg>vellhaul@mailnest.com.au</div>
    </div>
  </section>

  <section class="card card-back red">
    <div class="back-band">
      <div class="square"></div>
      <div class="wordmark">Vell<br>Haulage<br>Contracting</div>
    </div>
  </section>

  <section class="card card-back charcoal">
    <div class="back-band">
      <div class="square"></div>
      <div class="wordmark">Vell<br>Haulage<br>Contracting</div>
    </div>
  </section>

</body>
</html>
```